Blue Heron IT Business Card - Clean, Simple

Need a simple, clean standard sized business card for an IT consulting business using existing logo and company colours. Background should be mainly white. Feel free to be creative but clean, simple, quiet design is preferred. Font is specified in logo but any sans serif fonts work.

Contact Information for card is as follows (doesn't need to be in this exact order):

Martin Calloway
Owner
martin@blueheronit.ca
705-391-2586
www.blueheronit.ca

Target Market(s)

Small to medium sized business.

Industry/Entity Type

IT Consulting

Contact Information for Business Card

Logo and contact info.

Font styles to use
Sans Serif

Colors
EE7325
F08F49
F5BC92
FAE3D3
FDF4ED

Requirements
Must have
• All white or mostly white background.

```html
<!DOCTYPE html>
<html lang="en">
<head>
<meta charset="utf-8">
<title>Blue Heron IT Business Card</title>
<link rel="stylesheet" href="https://fonts.googleapis.com/css2?family=Montserrat:wght@400;500;600;700&display=swap">
<style>
  :root {
    --orange: #EE7325;
    --orange-soft: #F08F49;
    --ink: #333333;
    --ink-soft: #3d3d3d;
    --paper: #ffffff;
    --paper-shade: #f6f6f6;
    --backdrop: #3a3a3a;
  }
  html, body {
    margin: 0;
    padding: 0;
    width: 1200px;
    height: 1200px;
    overflow: hidden;
    background: var(--backdrop);
    font-family: "Montserrat", sans-serif;
  }
  .sheet {
    width: 1200px;
    height: 1200px;
    display: flex;
    flex-direction: column;
    align-items: center;
    justify-content: center;
    gap: 60px;
  }
  .card {
    position: relative;
    width: 840px;
    height: 480px;
    background: linear-gradient(180deg, var(--paper) 0%, var(--paper) 60%, var(--paper-shade) 100%);
    border-radius: 40px;
    box-shadow: 0 4px 0 var(--orange), 0 18px 30px rgba(0,0,0,0.45);
    overflow: hidden;
  }
  /* Front */
  .card--front .contact {
    position: absolute;
    left: 72px;
    bottom: 92px;
  }
  .contact__name {
    margin: 0;
    font-size: 34px;
    font-weight: 500;
    color: var(--orange);
    letter-spacing: -0.3px;
    line-height: 1;
  }
  .contact__name strong { font-weight: 600; }
  .contact__role {
    margin: 6px 0 26px 10px;
    font-size: 15px;
    font-weight: 400;
    letter-spacing: 1px;
    color: var(--ink);
  }
  .contact__list {
    list-style: none;
    margin: 0;
    padding: 0 0 0 10px;
  }
  .contact__item {
    display: flex;
    align-items: center;
    gap: 14px;
    font-size: 22px;
    color: var(--ink);
    margin-bottom: 12px;
  }
  .contact__item svg { width: 28px; height: 28px; flex: none; }
  .brand {
    position: absolute;
    display: flex;
    align-items: center;
    gap: 14px;
    color: var(--ink-soft);
    font-weight: 600;
    letter-spacing: -1px;
    white-space: nowrap;
  }
  .brand__dot {
    border-radius: 50%;
    background: var(--orange);
    flex: none;
  }
  .card--front .brand {
    right: 70px;
    top: 190px;
    font-size: 50px;
  }
  .card--front .brand__dot { width: 26px; height: 26px; }
  /* Back */
  .card--back .brand {
    left: 50%;
    top: 50%;
    transform: translate(-50%, -50%);
    font-size: 66px;
    gap: 18px;
  }
  .card--back .brand__dot { width: 34px; height: 34px; }
</style>
</head>
<body>
<main class="sheet">
  <section class="card card--front" aria-label="Business card front">
    <div class="contact">
      <h1 class="contact__name"><strong>Martin</strong> Calloway</h1>
      <p class="contact__role">OWNER</p>
      <ul class="contact__list">
        <li class="contact__item">
          <svg viewBox="0 0 24 24" aria-hidden="true"><path fill="var(--orange)" d="M6.6 10.8c1.4 2.8 3.8 5.1 6.6 6.6l2.2-2.2c.3-.3.7-.4 1-.2 1.1.4 2.3.6 3.6.6.6 0 1 .4 1 1V20c0 .6-.4 1-1 1C10.6 21 3 13.4 3 4c0-.6.4-1 1-1h3.5c.6 0 1 .4 1 1 0 1.3.2 2.5.6 3.6.1.3 0 .7-.2 1z"/></svg>
          <span>705-391-2586</span>
        </li>
        <li class="contact__item">
          <svg viewBox="0 0 24 24" aria-hidden="true" fill="none" stroke="var(--orange)" stroke-width="1.8"><circle cx="12" cy="12" r="9.5"/><ellipse cx="12" cy="12" rx="4" ry="9.5"/><path d="M2.5 12h19M4 7h16M4 17h16"/></svg>
          <span>www.blueheronit.ca</span>
        </li>
        <li class="contact__item">
          <svg viewBox="0 0 24 24" aria-hidden="true"><rect x="2" y="5" width="20" height="14" fill="var(--orange)"/><path d="M2 5l10 8 10-8" fill="none" stroke="#fff" stroke-width="1.6"/></svg>
          <span>martin@blueheronit.ca</span>
        </li>
      </ul>
    </div>
    <div class="brand"><span class="brand__dot"></span><span class="brand__name">Blue Heron IT</span></div>
  </section>

  <section class="card card--back" aria-label="Business card back">
    <div class="brand"><span class="brand__dot"></span><span class="brand__name">Blue Heron IT</span></div>
  </section>
</main>
</body>
</html>
```